Combat Sports news website design

Redesigning our existing website to make it more modern, responsive and suitable for our needs. The design needs to take in to account all aspects of our current website structure and services. View the existing website at https://www.bramblewire.co.nz

Particular attention should be paid to our livestream service, which is growing and needs to be much more user friendly to the current experience.

The homepage, article listings and article pages need designs.

Target Market(s)

Combat sports fans

Industry/Entity Type

Media

Coding

Coded - Design and coding required

Number of Pages Required

5+ page

Font styles to use
Sans Serif

Requirements
Must have
• All the functionality of the existing website must be taken in to account, and improved upon.
New design must incorporate our existing logo/colour scheme as this has only just been designed.

```html
<!DOCTYPE html>
<html lang="en">
<head>
<meta charset="utf-8">
<title>Bramblewire – Marlow-Winter unfazed by Hazzard's undefeated record</title>
<link rel="stylesheet" href="https://fonts.googleapis.com/css2?family=Oswald:wght@400;500;700&family=Roboto:wght@400;500;700&display=swap">
<style>
:root{
  --nav:#333333;
  --subnav:#232323;
  --red:#c41f2a;
  --ink:#1e1e1e;
  --muted:#8a8a8a;
  --pale:#c9c9c9;
  --line:#dedede;
  --adbox:#efefef;
  --footer:#333333;
  --field:#4a4a4a;
}
*{margin:0;padding:0;box-sizing:border-box}
html,body{width:1200px;height:2948px;overflow:hidden;background:#fff}
body{position:relative;font-family:"Roboto",sans-serif;color:var(--ink)}
.abs{position:absolute}

/* top navigation */
.topnav{left:0;top:0;width:1200px;height:60px;background:var(--nav)}
.topnav a{position:absolute;top:19px;color:#fff;text-decoration:none;font-family:"Oswald",sans-serif;font-weight:500;font-size:15px;text-transform:uppercase}
.topnav .active{top:15px;font-size:20px}
.topnav .underline{position:absolute;left:221px;top:57px;width:134px;height:3px;background:var(--red)}
.brand{position:absolute;left:560px;top:13px;font-family:"Oswald",sans-serif;font-weight:700;font-size:22px;color:#fff;letter-spacing:.5px}
.subnav{left:0;top:60px;width:1200px;height:49px;background:var(--subnav)}
.subnav a{position:absolute;top:15px;color:#8d8d8d;text-decoration:none;font-family:"Oswald",sans-serif;font-weight:500;font-size:14px}
.subnav a.on{color:#fff}

/* hero */
.hero{left:0;top:109px;width:1200px;height:622px;background:radial-gradient(ellipse 320px 420px at 50% 45%,#6b5448 0%,#3a2d2a 45%,#0c0c0e 100%)}
.hero .arrow{position:absolute;top:258px}
.hero h1{position:absolute;left:165px;top:340px;width:660px;font-family:"Oswald",sans-serif;font-weight:700;font-size:44px;line-height:44px;color:#fff;letter-spacing:-.5px}
.hero .dek{position:absolute;left:165px;top:439px;width:575px;font-weight:700;font-size:14.5px;line-height:18px;color:#fff}
.hero .rule{position:absolute;left:165px;top:518px;width:870px;height:1px;background:#9a9a9a}
.hero .meta{position:absolute;top:528px;font-family:"Oswald",sans-serif;font-weight:500;font-size:9px;color:#fff}

/* article */
.sidebar-divider{left:796px;top:731px;width:1px;height:1805px;background:#ececec}
.shares{left:121px;top:795px;width:567px;height:26px;border-bottom:1px solid #cfcfcf}
.shares .count{position:absolute;right:235px;top:3px;font-weight:700;font-size:14px;color:#555}
.shares .sep{position:absolute;right:224px;top:2px;width:1px;height:18px;background:#ccc}
.shares .ico{position:absolute;top:3px}
.article{left:123px;width:565px;font-size:13.4px;line-height:13.7px;color:#222}
.article p{margin-bottom:14.6px}
.article .q{font-weight:700}
.article .note{color:var(--muted);font-size:14px;line-height:15.5px}
.article .note b{font-weight:500;color:#888}
.figure{left:121px;top:1581px;width:567px;height:402px;background:#0a0a0a}
.figure .photo{position:absolute;left:92px;top:0;width:383px;height:402px;background:linear-gradient(180deg,#6b5a50 0%,#a48068 40%,#3b2f2b 80%,#141414 100%)}
.figure .next{position:absolute;left:444px;top:230px}
.caption{left:121px;top:1993px;width:567px;font-size:9px;color:#aaa;font-weight:500}
.caption .src{position:absolute;right:35px;top:0}

/* sidebar */
.side-title{font-family:"Oswald",sans-serif;font-weight:500;font-size:17px;text-align:center;color:#222;width:300px}
.adbox{width:279px;height:198px;background:var(--adbox);display:flex;align-items:center;justify-content:center;text-align:center;font-family:"Oswald",sans-serif;font-weight:500;font-size:30px;line-height:42px;color:#dadada}
.headline{left:832px;width:300px}
.headline .date{font-size:8px;color:#444;margin-bottom:3px}
.headline .title{font-weight:700;font-size:14.5px;line-height:17px;color:var(--red);width:285px}
.card{left:842px;width:313px;height:112px;background:#fff;box-shadow:2px 2px 6px rgba(0,0,0,.06)}
.card .thumb{position:absolute;left:0;top:0;width:142px;height:112px}
.card .cat{position:absolute;left:164px;top:17px;font-weight:700;font-size:9.5px;color:var(--red)}
.card .ttl{position:absolute;left:164px;top:35px;width:135px;font-family:"Oswald",sans-serif;font-weight:500;font-size:12.5px;line-height:19px;color:#111}
.card .more{position:absolute;left:164px;top:92px;font-size:7px;font-weight:700;color:var(--red)}
.opinion .lead{position:absolute;left:839px;top:2331px;font-size:18px;color:#333}
.opt{position:absolute;font-family:"Oswald",sans-serif;font-weight:500;font-size:23px;color:#d2d2d2}
.opt.on{color:var(--red)}
.btn{position:absolute;top:2447px;height:37px;background:var(--red);color:#fff;font-family:"Oswald",sans-serif;font-weight:700;font-size:19px;display:flex;align-items:center;justify-content:center}

/* footer */
.footer{left:0;top:2536px;width:1200px;height:412px;background:var(--footer)}
.footer .logo{position:absolute;left:82px;top:20px;font-family:"Oswald",sans-serif;font-weight:700;font-size:44px;line-height:46px;color:#fff}
.footer .editor{position:absolute;left:82px;top:152px;font-weight:700;font-size:19px;color:#9a9a9a}
.footer .bio{position:absolute;left:82px;top:176px;width:243px;font-size:14px;line-height:16.6px;color:#8f8f8f;text-align:justify}
.footer h4{position:absolute;font-weight:500;font-size:13px;color:#5e5e5e}
.footer ul{position:absolute;list-style:none;font-size:15px;line-height:20.8px;color:#d0d0d0;letter-spacing:.4px}
.footer .field{position:absolute;left:858px;width:180px;height:23px;background:var(--field);font-size:10px;color:#cfcfcf;padding:6px 10px}
.footer .message{width:259px;height:152px}
.footer .submit{position:absolute;left:858px;top:348px;width:79px;height:22px;background:var(--red);color:#fff;font-family:"Oswald",sans-serif;font-weight:700;font-size:14px;text-align:center;line-height:22px}
.footer .social{position:absolute;top:310px}
.footer .copy{position:absolute;left:82px;top:384px;font-size:8.5px;color:#aaa}
.footer .help{position:absolute;left:452px;top:382px;font-size:13px;color:#5e5e5e;font-weight:500}
.footer .mail{position:absolute;left:578px;top:380px;font-size:15px;color:#c8c8c8}
</style>
</head>
<body>

<header class="abs topnav">
  <a style="left:137px">Home</a>
  <a class="active" style="left:244px">Categories</a>
  <a style="left:390px">Live Events</a>
  <span class="brand">BRAMBLEWIRE</span>
  <a style="left:744px">Contact Us</a>
  <a style="left:853px">About Us</a>
  <a style="left:960px">Login &nbsp;/&nbsp; Register</a>
  <svg class="abs" style="left:1096px;top:20px" width="20" height="20" viewBox="0 0 20 20"><circle cx="8" cy="8" r="6" fill="none" stroke="#fff" stroke-width="2.2"/><line x1="12.5" y1="12.5" x2="18" y2="18" stroke="#fff" stroke-width="2.4"/></svg>
  <span class="underline"></span>
</header>

<nav class="abs subnav">
  <a style="left:137px">MMA</a>
  <a class="on" style="left:197px">KICKBOXING</a>
  <a style="left:293px">BOXING</a>
  <a style="left:365px">WRESTLING</a>
  <a style="left:459px">UCW</a>
  <a style="left:513px">PRIMEFC</a>
</nav>

<section class="abs hero" role="img" aria-label="Portrait of a tattooed fighter lit against a dark background">
  <svg class="arrow" style="left:44px" width="20" height="34" viewBox="0 0 20 34"><polyline points="17,3 4,17 17,31" fill="none" stroke="#bdbdbd" stroke-width="3.5"/></svg>
  <svg class="arrow" style="left:1126px" width="20" height="34" viewBox="0 0 20 34"><polyline points="3,3 16,17 3,31" fill="none" stroke="#bdbdbd" stroke-width="3.5"/></svg>
  <h1>Marlow-Winter unfazed by Hazzard’s undefeated record</h1>
  <p class="dek">This Saturday night, in the main event of KMT Presents: To the Top in Hamilton, local fighter Jace Marlow-Winter faces undefeated Toby Hazzard under full Thai rules.</p>
  <span class="rule"></span>
  <span class="meta" style="left:165px">BY HENRY GREAVES • 08 DEC, 2020</span>
  <span class="meta" style="right:165px">PHOTO: COLIN TARRANT</span>
</section>

<div class="abs sidebar-divider"></div>

<div class="abs shares">
  <span class="count">417 Shares</span>
  <span class="sep"></span>
  <svg class="ico" style="right:196px" width="14" height="16"><circle cx="7" cy="8" r="6" fill="#555"/></svg>
  <svg class="ico" style="right:155px" width="16" height="16"><circle cx="8" cy="8" r="6.5" fill="#555"/></svg>
  <svg class="ico" style="right:114px" width="16" height="16"><circle cx="8" cy="8" r="6.5" fill="#555"/></svg>
  <svg class="ico" style="right:73px" width="16" height="16"><circle cx="8" cy="8" r="6.5" fill="#555"/></svg>
  <svg class="ico" style="right:36px" width="18" height="16" viewBox="0 0 18 16"><rect x="4" y="1" width="10" height="4" fill="#555"/><rect x="1" y="5" width="16" height="7" rx="1" fill="#555"/><rect x="4" y="10" width="10" height="5" fill="#fff" stroke="#555" stroke-width="1.5"/></svg>
  <svg class="ico" style="right:0" width="19" height="15" viewBox="0 0 19 15"><rect x="0" y="1" width="19" height="13" rx="1" fill="#555"/><polyline points="1,2 9.5,8.5 18,2" fill="none" stroke="#fff" stroke-width="1.4"/></svg>
</div>

<article class="abs article" style="top:847px">
  <p>Both men are multiple-time New Zealand champions, though the fight will not be for a title. It will be contested over five two-minute rounds and will follow a huge fight card featuring five New Zealand title fights.</p>
  <p>In Jace’s most recent fight he defeated Kellan Locke-Carmody on October 31 to win the IFKA New Zealand 75kg full Thai rules title. Marlow-Winter is a four-time NZ champion under various sanctioning bodies and was a quarter-finalist in this year’s 75kg Crown of the Ring tournament.</p>
  <p>Bramblewire asked Jace a few questions ahead of Saturday’s main event fight.</p>
  <p class="q">Hey Jace. This weekend was originally planned as a four-man tournament. Did the others fall out with injury?</p>
  <p>“Cade [Nesbitt] took a fight at Capital Clash against someone he’d fought before, wanting to get one back up on him.</p>
  <p>“Terrell [Mountford] got a bit injured from fighting Red Garnet on the Ready to Fight show.”</p>
  <p class="q">This fight is still for the tournament prize money? How much?</p>
  <p>“I’m pretty sure it’s for $1500 – winner takes all.”</p>
  <p class="q">Does the fight being five two-minute rounds mean we can expect a high pace?</p>
  <p>“It kinda just depends on how the fight plays out, it usually does mean that but I think it just depends on the game of each fighter and how it all comes together.</p>
  <p>“Some people have a higher pace, some people pick their shots.”</p>
  <p class="q">Have you researched your opponent? How would you describe the style of Toby Hazzard?</p>
  <p>“Yeah, I’ve seen a little bit, it is pretty high pace. I haven’t looked too much into him, but I’m just sorta working on my own game.”</p>
  <p class="q">Does fighting an undefeated opponent make you think differently about the fight?</p>
  <p>“Nah, not really, because in the end it’s just another person. We were all undefeated until we lost one.”</p>
  <p class="q">What is your prediction for Saturday, how does the fight go?</p>
  <p>“I just wanna get in there and have fun. I’m not going in there to lose.”</p>
  <p class="q">Your last fight with Kellan was fun to watch. It looked like you cut him with punches, or was it something else?</p>
  <p>“Nah, I got him in the corner and threw my knee up as his head went down and he went straight into it. It was just a bit of timing.”</p>
</article>

<figure class="abs figure">
  <div class="photo" role="img" aria-label="Two shirtless fighters in gloves posing together after their bout"></div>
  <svg class="next" width="20" height="20" viewBox="0 0 20 20"><circle cx="10" cy="10" r="9" fill="rgba(255,255,255,.55)"/><polyline points="8,5 13,10 8,15" fill="none" stroke="#333" stroke-width="2"/></svg>
</figure>
<div class="abs caption">Jace Marlow-Winter and Kellan Locke-Carmody after their bout on Crown of Kings 9 in October
  <span class="src">SOURCE</span>
  <svg class="abs" style="right:5px;top:-2px" width="13" height="13"><circle cx="6.5" cy="6.5" r="5.5" fill="#cfcfcf"/></svg>
</div>

<article class="abs article" style="top:2031px">
  <p class="q">How do you think your game has evolved in the last couple of years?</p>
  <p>“Whether it’s wins or losses, we try to take it back to the drawing board and pick up where we went wrong or right.</p>
  <p>“We keep pressing the good things and working on the bad things. You’ll never be perfect, so there’s always things to look at from any fight, always room to grow.”</p>
  <p class="q">You have a Vaultfall tattoo. Do you still make time for video games?</p>
  <p>“It’s more surprising that I make time for training, haha.</p>
  <p>“My whole right arm is video games, and my left shin is anime, outside of training and everything, in my own time, I just like to kick back and relax.”</p>
  <p class="q">Have you seen the new Summit Muay Thai Warrior series? If they do a 75kg one will we see you in there?</p>
  <p>“I’m jealous as, haha. Yeah for sure man, definitely. That’s a mean idea. It’s like a more convenient and more practical eight-man.</p>
  <p>“It keeps the fighters each time at 100% as opposed to a standard eight-man where it comes down to injuries that fighters sustain in earlier fights.</p>
  <p class="q">Thanks for the interview Jace. All the best for this Saturday.</p>
  <p class="note">You can follow Jace Marlow-Winter on his social page: <b>@_jacemw_</b> They will fight this Saturday night in the main event of KMT Fight Night Presents: To the Top.</p>
  <p class="note">The event is run by Tawhiri Muay Thai and takes place at the KMT gym at 14 Kowhai Lane, Hamilton, with the first fight from 6:30pm. Tickets are available from Clarissa on <b>021 555 0134</b></p>
</article>

<!-- sidebar -->
<h3 class="abs side-title" style="left:832px;top:765px">ADVERTISEMENT</h3>
<div class="abs adbox" style="left:842px;top:805px">YOUR<br>AD<br>HERE</div>

<h3 class="abs side-title" style="left:832px;top:1053px">LATEST HEADLINES</h3>
<div class="abs headline" style="top:1087px"><p class="date">Wednesday 28 Apr, 2021</p><p class="title">Mara Jeune looking to avenge her only loss</p></div>
<div class="abs headline" style="top:1133px"><p class="date">Wednesday 28 Apr, 2021</p><p class="title">Rewi Stallard steps into Summit 80kg division on short notice</p></div>
<div class="abs headline" style="top:1194px"><p class="date">Wednesday 28 Apr, 2021</p><p class="title">Five WFKN New Zealand Cup winners crowned at Ready to Fight 9</p></div>
<div class="abs headline" style="top:1257px"><p class="date">Wednesday 28 Apr, 2021</p><p class="title">Mara Jeune looking to avenge her only loss</p></div>
<div class="abs headline" style="top:1301px"><p class="date">Wednesday 28 Apr, 2021</p><p class="title">Mara Jeune looking to avenge her only loss</p></div>
<div class="abs headline" style="top:1345px"><p class="date">Wednesday 28 Apr, 2021</p><p class="title">Rewi Stallard steps into Summit 80kg division on short notice</p></div>

<h3 class="abs side-title" style="left:832px;top:1439px">ADVERTISEMENT</h3>
<div class="abs adbox" style="left:842px;top:1476px">YOUR<br>AD<br>HERE</div>

<h3 class="abs side-title" style="left:849px;top:1723px">OTHER ARTICLES</h3>
<div class="abs card" style="top:1763px">
  <div class="thumb" role="img" aria-label="Referee raising a winner's arm in a ring" style="background:linear-gradient(180deg,#5d6f86,#c9c9cf 70%,#8b8f99)"></div>
  <span class="cat">UCW</span><p class="ttl">RTF9 Results: Mara Jeune wins RTF9 debut</p><span class="more">READ MORE</span>
</div>
<div class="abs card" style="top:1889px">
  <div class="thumb" role="img" aria-label="Kickboxer with gloves raised in the ring" style="background:linear-gradient(180deg,#1b2b4a,#7a5a4c 55%,#2a2a2e)"></div>
  <span class="cat">KICKBOXING</span><p class="ttl">Hollis aiming for international fight career</p><span class="more">READ MORE</span>
</div>
<div class="abs card" style="top:2015px">
  <div class="thumb" role="img" aria-label="Two boxers exchanging punches under green lights" style="background:linear-gradient(135deg,#1e8a3e,#2e4d6b 55%,#151c24)"></div>
  <span class="cat">BOXING</span><p class="ttl">KMT Fight Night results last Saturday</p><span class="more">READ MORE</span>
</div>
<div class="abs card" style="top:2141px">
  <div class="thumb" role="img" aria-label="Fighter holding a championship belt" style="background:linear-gradient(180deg,#2f4f8a,#a07a62 55%,#3c2e2a)"></div>
  <span class="cat">MMA</span><p class="ttl">Sheridan two-time South Island champ</p><span class="more">READ MORE</span>
</div>

<section class="opinion">
  <h3 class="abs side-title" style="left:838px;top:2302px">OPINION AREA</h3>
  <p class="lead">Select your prefered combat sport</p>
  <span class="opt" style="left:839px;top:2362px">MMA</span>
  <span class="opt on" style="left:907px;top:2362px">Wrestling</span>
  <span class="opt" style="left:1017px;top:2362px">Kickboxing</span>
  <span class="opt" style="left:839px;top:2394px">Boxing</span>
  <span class="opt" style="left:922px;top:2394px">Muay Thai</span>
  <span class="opt" style="left:1030px;top:2394px">UCW</span>
  <span class="opt" style="left:1087px;top:2394px">ALL</span>
  <span class="btn" style="left:839px;width:133px">VOTE</span>
  <span class="btn" style="left:984px;width:133px">VIEW RESULTS</span>
</section>

<footer class="abs footer">
  <div class="logo">BRAMBLE<br>WIRE</div>
  <p class="editor">Lavinia Pountney</p>
  <p class="bio">Lavinia has worked in the media industry since she was 15-years-old. She has worked in both radio and print, and is the co-founder and editor-in-chief of Bramblewire. As well as being the Bramblewire Editor, she focuses on writing for muti-discipline combat sports.</p>

  <h4 style="left:452px;top:37px">SITE MAP</h4>
  <ul style="left:452px;top:58px"><li>Home</li><li>MMA</li><li>Kickboxing</li><li>Boxing</li><li>Wrestling</li><li>UCW</li><li>PRIMEFC</li><li>Live events</li></ul>
  <h4 style="left:612px;top:37px">USEFULL LINKS</h4>
  <ul style="left:612px;top:58px"><li>Site Terms</li><li>Advertisement</li><li>Contact us</li><li>Privacy</li></ul>

  <h4 style="left:452px;top:274px">GET IN TOUCH</h4>
  <svg class="social" style="left:452px" width="190" height="24" aria-label="Social channels">
    <circle cx="8" cy="12" r="9" fill="#6a6a6a"/><circle cx="57" cy="12" r="10" fill="#6a6a6a"/><circle cx="111" cy="12" r="10" fill="#6a6a6a"/><circle cx="167" cy="12" r="10" fill="#6a6a6a"/>
  </svg>

  <h4 style="left:858px;top:37px">CONTACT US</h4>
  <div class="field" style="top:61px">First name</div>
  <div class="field" style="top:92px">Last name</div>
  <div class="field" style="top:123px">Email</div>
  <div class="field" style="top:154px">Phone / Mobile</div>
  <div class="field message" style="top:186px">Message</div>
  <div class="submit">Submit</div>

  <p class="copy">Copyright © 2021-2022 BRAMBLEWIRE All Rights Reserved</p>
  <p class="help">NEED HELP?</p>
  <svg class="abs" style="left:548px;top:383px" width="22" height="16" viewBox="0 0 22 16"><rect width="22" height="16" rx="1" fill="#8a8a8a"/><polyline points="1,1 11,9 21,1" fill="none" stroke="#333" stroke-width="1.5"/></svg>
  <p class="mail">newsdesk@bramblewire.co.nz</p>
</footer>

</body>
</html>
```